Health supplement brand needs a new logo for flagship product launch

I have attached a Word document to the brief which gives more detail.

There are 3 different products that we will sell. The label should be interchangeable across all 3 products, where only the colours change. This requires both a selection of a font typface to match our style and a new image embedded in the logo.

Target Market(s)

The target customer is women aged between 25 and 60. We would like to cross over between both audiences, without ruling one out

Font styles to use
Sans Serif

Requirements
Must have
• - It must be eye catching, i.e. people need to stop scrolling when they see it.
- It must have contemporary colours that are popular with women, i.e. pinks, apricots, dark greens, mustards, etc
- The image needs to be very feminine, just like the target audience
- The label must evoke some emotion, yet still be a little bit fun without being too serious.
- The label must use this image below as the main foundation. I have included the EPS file with this email.
Nice to have
• - We want to be somewhere in the middle, as in, the right price point accessible for most people, but still with a bit of class, fun and femininity
Should not have
• - We also don’t want it to look like “just another” nutritional brand selling Marrin Staples

```html
<!DOCTYPE html>
<html lang="en">
<head>
<meta charset="utf-8">
<title>Lunavella label range</title>
<link rel="stylesheet" href="https://fonts.googleapis.com/css2?family=Lato:wght@400;700&family=Montserrat:wght@700&display=swap">
<style>
  :root {
    --backdrop: #5b5b5b;
    --paper: #ffffff;
    --ink: #1e1e1e;
    --tan: #e2cfc3;
    --mint: #7fc9ad;
    --renew: #f99ab0;
    --renew-text: #f48fa7;
    --balance: #f8bfb8;
    --balance-text: #f6bcb2;
    --glow: #f9d3b6;
    --glow-text: #f8cba8;
    --figure-a: #f6dfcc;
    --figure-b: #e7d3c7;
  }
  * { margin: 0; padding: 0; box-sizing: border-box; }
  html, body { width: 1200px; height: 464px; overflow: hidden; background: var(--backdrop); }
  .range { position: relative; width: 1200px; height: 464px; }
  .label {
    position: absolute; top: 39px; width: 333px; height: 385px;
    background: var(--paper); overflow: hidden;
  }
  .label--renew { left: 62px; --accent: var(--renew); --accent-text: var(--renew-text); }
  .label--balance { left: 433px; --accent: var(--balance); --accent-text: var(--balance-text); }
  .label--glow { left: 805px; --accent: var(--glow); --accent-text: var(--glow-text); }
  .label__frame { position: absolute; inset: 0; width: 100%; height: 100%; }
  .frame__band { fill: var(--accent); }
  .frame__curve { fill: none; stroke: var(--tan); stroke-width: 6; }
  .frame__base { fill: var(--tan); }
  .frame__floor { stroke: var(--ink); stroke-width: 1.5; }
  .brand {
    position: absolute; top: 12px; left: 0; width: 100%;
    display: flex; justify-content: center; align-items: center; gap: 6px;
    font-family: "Lato", sans-serif; font-weight: 400; font-size: 24px;
    letter-spacing: 5px; color: var(--ink);
  }
  .brand__mark { width: 13px; height: 13px; background: var(--mint); }
  .product {
    position: absolute; top: 90px; left: 0; width: 100%; text-align: center;
    font-family: "Lato", sans-serif; font-weight: 400; font-size: 27px;
    line-height: 34px; color: var(--ink); white-space: nowrap;
  }
  .variant {
    position: absolute; top: 125px; left: 0; width: 100%; text-align: center;
    font-family: "Montserrat", sans-serif; font-weight: 700; font-size: 18px;
    line-height: 24px; letter-spacing: 12px; padding-left: 12px;
    color: var(--accent-text); white-space: nowrap;
  }
  .details {
    position: absolute; top: 176px; left: 0; width: 100%; text-align: center;
    font-family: "Lato", sans-serif; font-size: 12.5px; line-height: 19px;
    color: var(--ink); white-space: nowrap;
  }
  .details__benefits span { margin: 0 5px; }
  .figure {
    position: absolute; left: 124px; top: 226px; width: 135px; height: 151px;
    border-radius: 45% 45% 25% 30% / 35% 35% 8% 8%;
    background: radial-gradient(ellipse at 50% 60%, var(--figure-a), var(--figure-b) 70%, rgba(231,211,199,0) 100%);
  }
</style>
</head>
<body>
<main class="range">

  <section class="label label--renew">
    <svg class="label__frame" viewBox="0 0 333 385" preserveAspectRatio="none" aria-hidden="true">
      <path class="frame__band" d="M0 0 H6 Q76 190 18 385 H0 Z"/>
      <path class="frame__band" d="M333 0 H327 Q257 190 315 385 H333 Z"/>
      <path class="frame__curve" d="M11 0 Q80 190 24 385"/>
      <path class="frame__curve" d="M322 0 Q253 190 309 385"/>
      <rect class="frame__base" x="0" y="377" width="333" height="8"/>
      <line class="frame__floor" x1="20" y1="377" x2="313" y2="377"/>
    </svg>
    <div class="brand"><span>LUNAVELLA</span><span class="brand__mark"></span></div>
    <h1 class="product">Gentle FIBER</h1>
    <p class="variant">RENEW</p>
    <div class="details">
      <p>Unflavoured 100% Bovine Collagen Powder</p>
      <p class="details__benefits">Hair<span>|</span>Skin<span>|</span>Nails<span>|</span>Joints<span>|</span>Muscles</p>
    </div>
    <div class="figure" role="img" aria-label="Line illustration of a seated woman seen from behind"></div>
  </section>

  <section class="label label--balance">
    <svg class="label__frame" viewBox="0 0 333 385" preserveAspectRatio="none" aria-hidden="true">
      <path class="frame__band" d="M0 0 H6 Q76 190 18 385 H0 Z"/>
      <path class="frame__band" d="M333 0 H327 Q257 190 315 385 H333 Z"/>
      <path class="frame__curve" d="M11 0 Q80 190 24 385"/>
      <path class="frame__curve" d="M322 0 Q253 190 309 385"/>
      <rect class="frame__base" x="0" y="377" width="333" height="8"/>
      <line class="frame__floor" x1="20" y1="377" x2="313" y2="377"/>
    </svg>
    <div class="brand"><span>LUNAVELLA</span><span class="brand__mark"></span></div>
    <h1 class="product">Glow COLLAGEN</h1>
    <p class="variant">BALANCE</p>
    <div class="details">
      <p>Unflavoured 100% Bovine Collagen Powder</p>
      <p class="details__benefits">Hair<span>|</span>Skin<span>|</span>Nails<span>|</span>Joints<span>|</span>Muscles</p>
    </div>
    <div class="figure" role="img" aria-label="Line illustration of a seated woman seen from behind"></div>
  </section>

  <section class="label label--glow">
    <svg class="label__frame" viewBox="0 0 333 385" preserveAspectRatio="none" aria-hidden="true">
      <path class="frame__band" d="M0 0 H6 Q76 190 18 385 H0 Z"/>
      <path class="frame__band" d="M333 0 H327 Q257 190 315 385 H333 Z"/>
      <path class="frame__curve" d="M11 0 Q80 190 24 385"/>
      <path class="frame__curve" d="M322 0 Q253 190 309 385"/>
      <rect class="frame__base" x="0" y="377" width="333" height="8"/>
      <line class="frame__floor" x1="20" y1="377" x2="313" y2="377"/>
    </svg>
    <div class="brand"><span>LUNAVELLA</span><span class="brand__mark"></span></div>
    <h1 class="product">Core COLLAGEN</h1>
    <p class="variant">SOFT GLOW</p>
    <div class="details">
      <p>Unflavoured 100% Bovine Collagen Powder</p>
      <p class="details__benefits">Hair<span>|</span>Skin<span>|</span>Nails<span>|</span>Joints<span>|</span>Muscles</p>
    </div>
    <div class="figure" role="img" aria-label="Line illustration of a seated woman seen from behind"></div>
  </section>

</main>
</body>
</html>
```